Property Management company

We need a design for our company Maplecrest Elder Commons. We are complex of apartments that we manage and operate. We do like the colors green or blue

Industry/Entity Type

Property Management,

Requirements
Must have
• color
Nice to have
• maybe be able to use as a watermark

```html
<!DOCTYPE html>
<html lang="en">
<head>
<meta charset="utf-8">
<title>Maplecrest Elder Commons Letterhead</title>
<link href="https://fonts.googleapis.com/css2?family=Poppins:wght@400;500&display=swap" rel="stylesheet">
<style>
  :root {
    --backdrop: #dcdcdc;
    --paper: #ffffff;
    --brand-blue: #2e90c5;
    --ink-dark: #1c1c1c;
    --text-light: #ffffff;
    --watermark: #f3f3f3;
  }
  html, body {
    margin: 0;
    padding: 0;
    width: 1200px;
    height: 947px;
    overflow: hidden;
    background: var(--backdrop);
    font-family: "Poppins", sans-serif;
  }
  .letterhead {
    position: absolute;
    left: 364px;
    top: 179px;
    width: 472px;
    height: 606px;
    background: var(--paper);
    overflow: hidden;
  }
  .header-band {
    position: absolute;
    left: 0; top: 0;
    width: 100%;
    height: 66px;
    background: var(--brand-blue);
  }
  .brand-block {
    position: absolute;
    left: 26px;
    top: 0;
    width: 160px;
    height: 91px;
    background: var(--ink-dark);
    display: flex;
    align-items: center;
    justify-content: center;
    gap: 7px;
  }
  .brand-dot {
    width: 12px;
    height: 12px;
    border-radius: 50%;
    background: var(--brand-blue);
    flex: none;
  }
  .brand-name {
    color: var(--brand-blue);
    font-weight: 500;
    font-size: 11px;
    line-height: 1.25;
    letter-spacing: 0.6px;
    text-transform: uppercase;
    margin: 0;
  }
  .contact-list {
    position: absolute;
    right: 28px;
    top: 21px;
    margin: 0;
    padding: 0;
    list-style: none;
    color: var(--text-light);
    font-size: 8.6px;
    line-height: 11.5px;
    text-align: right;
  }
  .contact-list li {
    display: flex;
    justify-content: flex-end;
    align-items: center;
    gap: 5px;
  }
  .contact-list svg {
    width: 9px;
    height: 9px;
    flex: none;
  }
  .watermark {
    position: absolute;
    left: 98px;
    top: 186px;
    width: 236px;
    height: 236px;
  }
  .footer-rule {
    position: absolute;
    left: 0;
    top: 579px;
    width: 100%;
    height: 3px;
    background: var(--brand-blue);
  }
  .footer-bar {
    position: absolute;
    left: 0;
    top: 582px;
    width: 100%;
    height: 24px;
    background: var(--ink-dark);
    color: var(--text-light);
    font-size: 9.6px;
    line-height: 24px;
    text-align: center;
  }
</style>
</head>
<body>
  <main class="letterhead">
    <div class="header-band"></div>

    <div class="brand-block">
      <span class="brand-dot"></span>
      <p class="brand-name">Maplecrest<br>Elder Commons</p>
    </div>

    <ul class="contact-list">
      <li>55501478236
        <svg viewBox="0 0 10 10" fill="none" stroke="#fff" stroke-width="1">
          <rect x="0.5" y="0.5" width="9" height="9" rx="1"/>
          <path d="M3 2.5 L4 4 L3.6 4.6 Q4.5 6 5.6 6.6 L6.2 6.1 L7.5 7 L7 8 Q4 7.5 2.5 3.5 Z" fill="#fff" stroke="none"/>
        </svg>
      </li>
      <li>office@maplecrestec.com
        <svg viewBox="0 0 10 10" fill="#fff">
          <rect x="0.5" y="2" width="9" height="6.5"/>
          <path d="M0.5 2 L5 5.8 L9.5 2" fill="none" stroke="#2e90c5" stroke-width="0.9"/>
        </svg>
      </li>
      <li>www.maplecrestec.com
        <svg viewBox="0 0 10 10" fill="none" stroke="#fff" stroke-width="0.9">
          <circle cx="5" cy="5" r="4.4"/>
          <ellipse cx="5" cy="5" rx="2" ry="4.4"/>
          <path d="M0.6 5 H9.4 M1.4 2.8 H8.6 M1.4 7.2 H8.6"/>
        </svg>
      </li>
    </ul>

    <svg class="watermark" viewBox="0 0 236 236" aria-hidden="true">
      <circle cx="118" cy="118" r="105" fill="none" stroke="var(--watermark)" stroke-width="26"/>
      <text x="118" y="113" text-anchor="middle" font-family="Poppins, sans-serif" font-weight="500" font-size="16" fill="var(--watermark)" letter-spacing="0.5">MAPLECREST</text>
      <text x="118" y="134" text-anchor="middle" font-family="Poppins, sans-serif" font-weight="500" font-size="16" fill="var(--watermark)" letter-spacing="0.5">ELDER COMMONS</text>
    </svg>

    <div class="footer-rule"></div>
    <footer class="footer-bar">Your Address line here, Country Code 0123456</footer>
  </main>
</body>
</html>
```